High end OB/Gyn medical practice in need of Open House Invitation

We are a well-established Ob/Gyn office in Massachusetts, KRE Ob/Gyn, P.C. that has recently opened a fourth location. Our offices are in Concord, Leominster, Sudbury and the open house is for our Westford office. We have Doctors, Nurse Midwives and Nurse Practitioners. We offer 3D ultrasound for our patients and same day appointments for urgent problems. We are having an Open House that is for other local medical professionals - such as Internal Medicine, Primary Care practices, pediatricians, etc. The date of the Open House is May 28th 5:00 to 7:00 for wine and hors d'oeuvres. The color palate for this office is red, white, grey and black. We are looking for upscale and professional. The names of our providers are Dr. Marta Velsing, Dr, Patrick Hulvane, Dr. Nora Paswick, Dorothea Kastrumenis, CNM, Hannah Tolvey, CNM, Karen Wessbruck, CNM, Miriam Colfield, CNM, Janet Ormsby, NP, Tara Vosko, NP.I have tried to attach logo and 3 pictures for reference and it would not attach - I can send by email. Colors of logo would need to be changed to match the color scheme for the office.
Target Market(s)
Other medical professionals and their practices - physicians,, midwives, nurse practitioners
Industry/Entity Type
Medical

```html
<!DOCTYPE html>
<html lang="en">
<head>
<meta charset="utf-8">
<title>Open House Invitation – KRE Ob/Gyn, P.C.</title>
<link rel="stylesheet" href="https://fonts.googleapis.com/css2?family=Tinos:wght@400;700&family=Arimo:ital,wght@0,400;1,400&display=swap">
<style>
  :root {
    --brand-red: #c01f2f;
    --paper: #ffffff;
    --placeholder-grey: #ececec;
    --ink-white: #ffffff;
  }
  html, body {
    margin: 0;
    padding: 0;
    overflow: hidden;
    background: var(--paper);
  }
  .invitation {
    position: relative;
    width: 1200px;
    height: 929px;
    overflow: hidden;
    background: var(--paper);
  }
  .red-panel {
    position: absolute;
    inset: 0;
    width: 1200px;
    height: 929px;
  }
  .headline {
    position: absolute;
    left: 44px;
    top: 84px;
    margin: 0;
    font-family: "Tinos", "Times New Roman", serif;
    font-weight: 700;
    font-size: 58px;
    line-height: 62px;
    color: var(--ink-white);
  }
  .team-title {
    position: absolute;
    left: 28px;
    top: 362px;
    margin: 0;
    font-family: "Arimo", Arial, sans-serif;
    font-weight: 400;
    font-size: 40px;
    line-height: 50px;
    color: var(--ink-white);
  }
  .provider-list {
    position: absolute;
    left: 30px;
    top: 468px;
    margin: 0;
    padding: 0;
    list-style: none;
    font-family: "Arimo", Arial, sans-serif;
    font-size: 29px;
    line-height: 43.3px;
    color: var(--ink-white);
  }
  .brand-mark {
    position: absolute;
    left: 632px;
    top: 70px;
    width: 176px;
    height: 176px;
    border-radius: 50%;
    background: var(--brand-red);
  }
  .brand-name {
    position: absolute;
    left: 679px;
    top: 270px;
    margin: 0;
    font-family: "Tinos", "Times New Roman", serif;
    font-weight: 700;
    font-size: 46px;
    line-height: 54px;
    color: var(--brand-red);
    white-space: nowrap;
  }
  .photo-slot {
    position: absolute;
    background: var(--placeholder-grey);
  }
  .photo-slot--small {
    left: 957px;
    top: 48px;
    width: 190px;
    height: 199px;
  }
  .photo-slot--wide {
    left: 614px;
    top: 447px;
    width: 530px;
    height: 164px;
  }
  .welcome-line {
    position: absolute;
    left: 635px;
    top: 650px;
    margin: 0;
    font-family: "Arimo", Arial, sans-serif;
    font-style: italic;
    font-size: 54px;
    line-height: 66px;
    color: var(--brand-red);
  }
  .event-details {
    position: absolute;
    left: 637px;
    top: 802px;
    margin: 0;
    font-family: "Arimo", Arial, sans-serif;
    font-size: 30px;
    line-height: 40px;
    color: var(--brand-red);
  }
</style>
</head>
<body>
  <main class="invitation">
    <svg class="red-panel" viewBox="0 0 1200 929" aria-hidden="true">
      <path d="M0 0 H444 C560 110 625 300 615 470 C605 650 540 820 452 929 H0 Z" fill="var(--brand-red)"/>
    </svg>

    <h1 class="headline">Open House<br>for local medical<br>professionals</h1>

    <h2 class="team-title">Meet our<br>Team of Providers</h2>
    <ul class="provider-list">
      <li>Dr. Marta Velsing</li>
      <li>Dr. Patrick Hulvane</li>
      <li>Dr. Nora Paswick</li>
      <li>Dorothea Kastrumenis, CNM</li>
      <li>Hannah Tolvey, CNM</li>
      <li>Karen Wessbruck, CNM</li>
      <li>Miriam Colfield, CNM</li>
      <li>Janet Ormsby, NP</li>
      <li>Tara Vosko, NP</li>
    </ul>

    <div class="brand-mark" aria-hidden="true"></div>
    <p class="brand-name">KRE Ob/Gyn, P.C.</p>

    <div class="photo-slot photo-slot--small" role="img" aria-label="Photo of the practice"></div>
    <div class="photo-slot photo-slot--wide" role="img" aria-label="Photo of the new Westford office"></div>

    <p class="welcome-line">Join us for wine<br>&amp; hors d'oeuvres!</p>
    <p class="event-details">May 28th &middot; 5:00 – 7:00 pm<br>at our new Westford office</p>
  </main>
</body>
</html>
```